Saveurs Du Matin

looking fo an e-commerce site something that will stand out the site domain will be saveursdumatin.example need somthing bold and refind as well; eye appealing and not too cartonish please visit our competetors to see waht we are going for they are (tastrovel.example, brenza4u.example and calvanopresses.example) this site should have multiple pages mainly looking for a layout to start the site and code.

PLEASE REMEMBER WE REQUIRE THE CODE....

Target Market(s)

anyone who loves food or is fasinated by it

Industry/Entity Type

E-Commerce

Requirements
Must have
• .an easy to work site that makes sense and that is not all over the place it should have in the navigation feature: Olive oils, Balsamic Vinegars, Misc. Vinegars and oils, Specialty salts, organic spices, Specialty Spices, Kitchen Tools. also pleas use our logo in the design i have attached below
Nice to have
• clean and some spices, salt, pepermills, morter and pistels, olive oils, trying to stick to a clean presentation
Should not have
• no cartoon figures or alike, anything too playfull

```html
<!DOCTYPE html>
<html lang="en">
<head>
<meta charset="utf-8">
<title>Saveurs Du Matin</title>
<link rel="stylesheet" href="https://fonts.googleapis.com/css2?family=Noto+Serif:wght@400;700&family=Arimo:wght@400;700&display=swap">
<style>
:root{
  --red:#c4161c;
  --red-dark:#9e1015;
  --brown:#8a3a12;
  --brown-dark:#5a2a12;
  --text:#555;
  --muted:#8a8a8a;
  --line:#d8d8d8;
  --footer:#e8e8ea;
  --white:#fff;
}
*{box-sizing:border-box;margin:0;padding:0}
html,body{width:800px;height:1200px;overflow:hidden;background:var(--white)}
body{position:relative;font-family:"Arimo",Arial,sans-serif;color:var(--text)}

.brand{position:absolute;left:74px;top:0;width:117px;height:118px;background:var(--white);border:4px solid var(--red-dark);display:flex;flex-direction:column;align-items:center;justify-content:center;gap:6px;z-index:3;box-shadow:0 1px 3px rgba(0,0,0,.2)}
.brand-mark{width:14px;height:14px;border-radius:50%;background:var(--red)}
.brand-name{font-family:"Noto Serif",Georgia,serif;font-size:12px;color:var(--red-dark);text-align:center;line-height:1.2}

.utility{position:absolute;left:474px;top:24px;font-size:6.5px;color:var(--red)}
.utility a{color:var(--red);text-decoration:none;margin-right:6px}
.phone{position:absolute;left:474px;top:40px;font-size:9px;letter-spacing:.5px;color:#333;display:flex;align-items:center;gap:3px}
.sep{position:absolute;top:26px;height:26px;border-left:1px dashed #bbb}
.cart{position:absolute;left:621px;top:29px;width:118px;height:20px;background:linear-gradient(#f4f4f4,#e6e6e6);display:flex;align-items:center;font-size:7.5px;color:#333}
.cart-icon{width:24px;height:20px;background:var(--red);display:flex;align-items:center;justify-content:center;margin-right:9px}

.hero{position:absolute;left:60px;top:68px;width:680px;height:308px;border:1px solid var(--line);padding:5px}
.hero-photo{width:100%;height:100%;background:linear-gradient(160deg,#f2ece4 0%,#d7a15c 40%,#c98a3e 60%,#7d4a22 100%);position:relative}
.main-nav{position:absolute;left:0;right:0;bottom:0;height:44px;background:rgba(250,240,222,.72);display:flex;align-items:center;justify-content:space-between;padding:0 11px 0 11px}
.main-nav a{font-family:"Noto Serif",Georgia,serif;font-weight:700;font-size:9.5px;color:var(--red-dark);text-decoration:none}
.main-nav span{font-size:9px;color:var(--red-dark)}

.section-title{position:absolute;left:68px;top:406px;font-family:"Noto Serif",Georgia,serif;font-weight:700;font-size:19px;color:var(--brown-dark)}
.section-title em{font-style:normal;color:var(--brown)}
.section-rule{position:absolute;left:62px;top:436px;width:677px;border-top:1px solid var(--line)}

.product{position:absolute;width:150px}
.product-frame{width:148px;height:130px;border:1px solid var(--line);padding:5px}
.product-photo{width:100%;height:100%}
.product-name{font-family:"Noto Serif",Georgia,serif;font-weight:700;font-size:12px;color:var(--red);margin-top:7px}
.product-desc{font-size:8.3px;line-height:11.5px;color:var(--text);margin-top:1px}
.btn{display:inline-block;margin-top:7px;width:58px;height:22px;line-height:22px;text-align:center;background:var(--red);color:var(--white);font-size:8.5px;font-weight:700;text-decoration:none;box-shadow:0 1px 0 var(--red-dark)}

.footer{position:absolute;left:0;top:955px;width:800px;height:245px;background:var(--footer);border-top:3px solid var(--red)}
.footer-col{position:absolute;top:50px}
.footer-col h3{font-family:"Noto Serif",Georgia,serif;font-weight:700;font-size:10.5px;color:#666;margin-bottom:7px}
.footer-col a{display:block;font-size:9px;color:var(--muted);text-decoration:none;line-height:13.6px}
.social{display:flex;gap:11px;margin-top:4px}
.social span{width:20px;height:20px;background:linear-gradient(#fafafa,#dcdcdc);border-radius:3px;box-shadow:0 1px 1px rgba(0,0,0,.15)}
.footer-rule{position:absolute;left:78px;top:150px;width:644px;border-top:1px solid #d2d2d4}
.copyright{position:absolute;left:78px;top:182px;font-size:8.5px;color:var(--muted)}
</style>
</head>
<body>

<header>
  <div class="brand">
    <span class="brand-mark"></span>
    <span class="brand-name">Saveurs Du Matin</span>
  </div>
  <span class="sep" style="left:446px"></span>
  <nav class="utility"><a href="#">Help</a><a href="#">Login</a><a href="#">My Shortlist (0)</a></nav>
  <div class="phone">
    <svg width="11" height="9" viewBox="0 0 11 9"><path d="M1 3 Q5.5 -1 10 3 L8.5 4.5 L7 3.5 L4 3.5 L2.5 4.5 Z" fill="#1d5fa8"/><rect x="2" y="4.5" width="7" height="4" rx="1" fill="#1d5fa8"/></svg>
    1 555-010-4477
  </div>
  <span class="sep" style="left:591px"></span>
  <div class="cart">
    <span class="cart-icon">
      <svg width="13" height="10" viewBox="0 0 13 10"><path d="M0.5 1 H2.5 L4 7 H11 L12 3 H3" fill="none" stroke="#fff" stroke-width="1.2"/><circle cx="5" cy="9" r="0.9" fill="#fff"/><circle cx="10" cy="9" r="0.9" fill="#fff"/></svg>
    </span>
    <b>Cart:</b>&nbsp;0 items
  </div>
</header>

<section class="hero">
  <div class="hero-photo" role="img" aria-label="Spices in white dishes, peppercorns in a mortar and fresh herbs on a wooden table">
    <nav class="main-nav">
      <a href="#">Olive Oils</a><span>|</span>
      <a href="#">Balsamic Vinegars</a><span>|</span>
      <a href="#">Misc.</a><span>|</span>
      <a href="#">Vinegars &amp; Oils</a><span>|</span>
      <a href="#">Specialty Salts</a><span>|</span>
      <a href="#">Organic Spices</a><span>|</span>
      <a href="#">Specialty Spices</a><span>|</span>
      <a href="#">Kitchen Tools</a>
    </nav>
  </div>
</section>

<h2 class="section-title"><em>Featured</em> Products</h2>
<div class="section-rule"></div>

<main>
  <article class="product" style="left:60px;top:455px">
    <div class="product-frame"><div class="product-photo" role="img" aria-label="Olive oil bottle with olives" style="background:linear-gradient(135deg,#f4f2e6,#d8c64a 55%,#6d6a2a)"></div></div>
    <h3 class="product-name">Lorem Ipsum Dolor</h3>
    <p class="product-desc">totam rem aperia eaque ipsa quae inventore lorem ipsum dolor</p>
    <a class="btn" href="#">Details</a>
  </article>
  <article class="product" style="left:237px;top:455px">
    <div class="product-frame"><div class="product-photo" role="img" aria-label="Assorted spices in a wooden bowl" style="background:linear-gradient(135deg,#b66a2c,#8a4a22 50%,#d7a04a)"></div></div>
    <h3 class="product-name">Lorem Ipsum Dolor</h3>
    <p class="product-desc">totam rem aperia eaque ipsa quae inventore lorem ipsum dolor</p>
    <a class="btn" href="#">Details</a>
  </article>
  <article class="product" style="left:415px;top:457px">
    <div class="product-frame"><div class="product-photo" role="img" aria-label="Salt shaker and spilled salt" style="background:linear-gradient(160deg,#e6e8ec,#b8bcc4 60%,#f4f4f4)"></div></div>
    <h3 class="product-name">Lorem Ipsum Dolor</h3>
    <p class="product-desc">totam rem aperia eaque ipsa quae inventore lorem ipsum dolor</p>
    <a class="btn" href="#">Details</a>
  </article>
  <article class="product" style="left:591px;top:457px">
    <div class="product-frame"><div class="product-photo" role="img" aria-label="Wooden mortar and pestle" style="background:linear-gradient(180deg,#dfe6d8,#c8ad8c 60%,#4a3a2e)"></div></div>
    <h3 class="product-name">Lorem Ipsum Dolor</h3>
    <p class="product-desc">totam rem aperia eaque ipsa quae inventore lorem ipsum dolor</p>
    <a class="btn" href="#">Details</a>
  </article>

  <article class="product" style="left:60px;top:701px">
    <div class="product-frame"><div class="product-photo" role="img" aria-label="Pair of wooden pepper mills" style="background:linear-gradient(90deg,#bfc3ca,#a86a3a 30%,#c9cdd3 50%,#a86a3a 75%,#bfc3ca)"></div></div>
    <h3 class="product-name">Lorem Ipsum Dolor</h3>
    <p class="product-desc">totam rem aperia eaque ipsa quae inventore lorem ipsum dolor</p>
    <a class="btn" href="#">Details</a>
  </article>
  <article class="product" style="left:237px;top:701px">
    <div class="product-frame"><div class="product-photo" role="img" aria-label="Piles of ground spices" style="background:linear-gradient(135deg,#a89a3a,#e08a1a 45%,#b0301a)"></div></div>
    <h3 class="product-name">Lorem Ipsum Dolor</h3>
    <p class="product-desc">totam rem aperia eaque ipsa quae inventore lorem ipsum dolor</p>
    <a class="btn" href="#">Details</a>
  </article>
  <article class="product" style="left:415px;top:701px">
    <div class="product-frame"><div class="product-photo" role="img" aria-label="Cinnamon sticks, star anise and cardamom" style="background:linear-gradient(135deg,#d8a86a,#8a4a1e 50%,#c88a4a)"></div></div>
    <h3 class="product-name">Lorem Ipsum Dolor</h3>
    <p class="product-desc">totam rem aperia eaque ipsa quae inventore lorem ipsum dolor</p>
    <a class="btn" href="#">Details</a>
  </article>
  <article class="product" style="left:591px;top:701px">
    <div class="product-frame"><div class="product-photo" role="img" aria-label="Glass oil and vinegar cruets" style="background:linear-gradient(180deg,#e4e6ea,#c8cbd0 55%,#b0702a 80%,#d8dadc)"></div></div>
    <h3 class="product-name">Lorem Ipsum Dolor</h3>
    <p class="product-desc">totam rem aperia eaque ipsa quae inventore lorem ipsum dolor</p>
    <a class="btn" href="#">Details</a>
  </article>
</main>

<footer class="footer">
  <div class="footer-col" style="left:84px">
    <h3>Information</h3>
    <a href="#">About</a><a href="#">Delivery</a><a href="#">Privacy Policy</a><a href="#">Terms &amp; Conditions</a>
  </div>
  <div class="footer-col" style="left:216px">
    <h3>Customer Service</h3>
    <a href="#">Contacts</a><a href="#">Returns</a><a href="#">Site Map</a>
  </div>
  <div class="footer-col" style="left:344px">
    <h3>Extras</h3>
    <a href="#">Spices</a><a href="#">Promotion Code</a><a href="#">Affiliates</a><a href="#">Specials</a>
  </div>
  <div class="footer-col" style="left:475px">
    <h3>My Account</h3>
    <a href="#">My Account</a><a href="#">Order History</a><a href="#">Wish List</a><a href="#">Newsletter</a>
  </div>
  <div class="footer-col" style="left:598px">
    <h3>Connect with Us</h3>
    <div class="social"><span></span><span></span><span></span></div>
  </div>
  <div class="footer-rule"></div>
  <p class="copyright">Copyright © 2012.&nbsp;&nbsp; Saveurs Du Matin.&nbsp; All Rights Reserved.</p>
</footer>

</body>
</html>
```